Talent Management Company needs an Employee Engagement Infographic

We need an interesting 1 page infographic that will help us to quickly and clearly share with clients the benefits Employee Engagement will have on their company's bottom line and culture.

You may get an idea of our brand and colors by visiting brightcrestpeople.com
We are a Talent Management Solutions company that specializes in helping our clients become great places to work with a strong focus on culture.

Attached is the information that should be included. We would like it to be on 1 page if possible. There is a lot of information attached, but it may be bulleted, shown with charts, graphics, etc.

Industry/Entity Type

It Company

```html
<!DOCTYPE html>
<html lang="en">
<head>
<meta charset="utf-8">
<title>Employee Engagement Infographic</title>
<link href="https://fonts.googleapis.com/css2?family=Didact+Gothic&family=Noto+Serif&display=swap" rel="stylesheet">
<style>
  :root {
    --sky-top: #8db6e2;
    --sky-low: #d3e3f4;
    --orange: #f6a623;
    --orange-pale: #fde6bf;
    --heading-blue: #1e88c8;
    --ink: #111111;
    --green: #6cbb45;
    --tab-grey: #4d4f55;
    --frame: #b5593a;
    --navy: #2a3990;
    --red-orange: #ef5a2a;
    --leaf: #3cb54a;
    --white: #ffffff;
  }
  * { box-sizing: border-box; margin: 0; padding: 0; }
  html, body { width: 834px; height: 1200px; overflow: hidden; background: var(--white); }
  .canvas {
    position: relative; width: 695px; height: 1000px;
    transform: scale(1.2); transform-origin: 0 0;
    font-family: "Didact Gothic", sans-serif; overflow: hidden;
    background: linear-gradient(180deg, var(--sky-top) 0%, var(--sky-low) 52%, var(--white) 56%, var(--white) 100%);
  }
  .backdrop { position: absolute; inset: 0; }
  .engagers { position: absolute; left: 58px; top: 88px; width: 300px; }
  .engagers h2 { font-weight: 400; font-size: 19.5px; color: var(--heading-blue); margin-bottom: 13px; }
  .engagers ul { list-style: none; font-size: 15.3px; line-height: 22px; color: var(--ink); }
  .engagers li::before { content: "\2022"; }
  .photo-frame {
    position: absolute; border: 1px solid var(--frame); padding: 4px; background: var(--white);
  }
  .photo-frame .photo { width: 100%; height: 100%; border: 1px solid var(--frame); }
  .photo-top { left: 481px; top: 45px; width: 200px; height: 266px; }
  .photo-top .photo { background: linear-gradient(180deg, #e9edf0 0%, #c9ccce 45%, #5a5b5e 100%); }
  .photo-side { left: 34px; top: 364px; width: 202px; height: 297px; }
  .photo-side .photo { background: linear-gradient(180deg, #d7dde3 0%, #e98a3b 40%, #c8c3bd 75%, #6d6f72 100%); }
  .tagline {
    position: absolute; left: 18px; top: 686px; width: 222px; text-align: center;
    font-family: "Noto Serif", serif; font-size: 20.5px; line-height: 28px; color: #222;
  }
  .t-enthusiastic { color: var(--orange); }
  .t-empowered { color: var(--navy); }
  .t-inspired { color: var(--red-orange); }
  .t-confident { color: var(--leaf); }
  .focus-tab {
    position: absolute; left: 337px; top: 346px; width: 228px; height: 37px;
    background: var(--tab-grey); color: var(--white); text-align: center;
    font-size: 22px; line-height: 37px;
  }
  .focus-panel { position: absolute; left: 252px; top: 376px; width: 430px; height: 592px; }
  .focus-panel svg { position: absolute; inset: 0; }
  .focus-list {
    position: relative; list-style: none; padding: 24px 28px 0 30px;
    color: var(--white); font-size: 15.2px; line-height: 20px;
  }
  .focus-list li { margin-bottom: 20px; }
  .focus-list li::before { content: "\2022"; }
</style>
</head>
<body>
<div class="canvas">
  <svg class="backdrop" width="695" height="1000" viewBox="0 0 695 1000" aria-hidden="true">
    <defs>
      <linearGradient id="bannerFade" x1="0" y1="0" x2="1" y2="0">
        <stop offset="0" stop-color="#f6a623"/>
        <stop offset="0.55" stop-color="#f9c46f"/>
        <stop offset="1" stop-color="#fde6bf"/>
      </linearGradient>
    </defs>
    <polygon points="0,40 380,40 478,178 478,196 392,325 0,325" fill="url(#bannerFade)"/>
    <polygon points="0,848 205,848 300,945 695,945 695,1000 0,1000" fill="#f6a623"/>
  </svg>

  <section class="engagers">
    <h2>What Engages Employees?</h2>
    <ul>
      <li>Relationship with Direct Manager</li>
      <li>Faith in Leadership</li>
      <li>Pride in what the company is doing</li>
      <li>Financial Incentives</li>
      <li>Rewards and Recognition</li>
      <li>Social connections</li>
      <li>Involvement in important decisions and processes</li>
      <li>Effective communication</li>
    </ul>
  </section>

  <div class="photo-frame photo-top"><div class="photo" role="img" aria-label="Bright open-plan office atrium with staff at tables"></div></div>
  <div class="photo-frame photo-side"><div class="photo" role="img" aria-label="Colourful multi-level office interior with orange walls"></div></div>

  <p class="tagline">Engaged employees are <span class="t-enthusiastic">Enthusiastic,</span> <span class="t-empowered">Empowered,</span> <span class="t-inspired">Inspired,</span> and <span class="t-confident">Confident</span></p>

  <section class="focus-panel">
    <svg width="430" height="592" viewBox="0 0 430 592" aria-hidden="true">
      <polygon points="4,6 60,3 140,7 220,2 300,6 380,3 426,5 424,90 427,200 423,320 426,450 424,586 340,589 250,585 160,590 70,586 3,589 6,470 2,340 5,210 3,100" fill="#6cbb45" stroke="#ffffff" stroke-width="3"/>
    </svg>
    <ul class="focus-list">
      <li>What are employees thinking - Listen to the employees – community forums, surveys, suggestion box, open-door policy</li>
      <li>Create a culture - Build a community, allow employees to feel comfortable and part of something bigger</li>
      <li>Show appreciation for impacts big and small - Rewards, recognition, appreciation, acknowledge good work</li>
      <li>Open, honest communication – show employees why what they do is so important</li>
      <li>Career path development – show employees where they can go and how they can get there – help them envision their future</li>
      <li>Interactions outside work – community outreach projects, organization wide celebrations/parties</li>
      <li>Tell the organization’s story – Strong employment branding, what does the company set out to accomplish</li>
    </ul>
  </section>
  <div class="focus-tab">Focus Points</div>
</div>
</body>
</html>
```